Stylish High End Wedding Videography/Films Website (BMTS)

We need a modern and high-end website look for our wedding video and films business. We films weddings all over the United Kingdom and at European destinations so need something to reflect our work. The website should be visually stunning with images and videos being the focal point as this is what our services are;

I have uploads of some items I like and the features the site needs to have. These have been taken from other websites using standout features.

We need the following pages;

1 - Homepage
2 - Films Index Page
3 - Individual Films Page
4 - Prices / Collection Page
5 - Reviews
6 - Options
7 - About
8 - Contact
9 - Blog Index
10 - Blog Page

All pages must be consistent so have a similar style.

Pages on menu:
Films
Prices
Reviews
Options
About
Contact

We require a responsive look too. Over 90% of our visitors access the website via their mobile devices.

Please use the colours from our logo to incorporate into the website.

Target Market(s)

Wedding Couples

Industry/Entity Type

Wedding Photography

Number of Pages Required

5+ page

Font styles to use
Sans Serif
Script

Requirements
Must have
• The logo must be in the centre of the menu at the top.

Social icons at the bottom of the page.

Use only two fonts including Lore which is supplied
Nice to have
• Different video for each page on the top header. This will play behind the menu.

```html
<!DOCTYPE html>
<html lang="en">
<head>
<meta charset="utf-8">
<title>BMTS – Options</title>
<link rel="stylesheet" href="https://fonts.googleapis.com/css2?family=Josefin+Sans:wght@300;400;600&family=Great+Vibes&display=swap">
<style>
:root{
  --ink:#3c3431;
  --taupe:#a59a93;
  --taupe-dark:#8f847d;
  --cream:#e5d9af;
  --gold:#b49a63;
  --white:#ffffff;
  --footer:#3e3531;
  --muted:#6f6661;
  --sans:'Josefin Sans', Arial, sans-serif;
  --script:'Great Vibes', cursive;
}
*{box-sizing:border-box;margin:0;padding:0}
html,body{width:1200px;height:3804px;overflow:hidden}
body{font-family:var(--sans);color:var(--ink);background:var(--white);position:relative}
section,header,footer{position:absolute;left:0;width:1200px}
.abs{position:absolute}
.photo{position:absolute}

/* Hero */
.hero{top:0;height:680px;background:#2a2421}
.hero .photo{inset:0;background:radial-gradient(ellipse at 60% 45%,#8a7b72 0%,#4d413b 45%,#221c19 100%)}
.nav{position:absolute;top:22px;left:0;width:1200px;height:40px}
.nav a{position:absolute;top:12px;color:var(--white);font-size:11px;letter-spacing:2.5px;text-decoration:none}
.brand{position:absolute;left:540px;top:4px;width:120px;text-align:center;color:var(--white)}
.brand .dot{display:block;width:14px;height:14px;border-radius:50%;background:var(--white);margin:0 auto 6px}
.brand span{font-size:15px;letter-spacing:4px;font-weight:600}
.play{position:absolute;left:556px;top:282px;width:88px;height:88px;border:2px solid var(--white);border-radius:50%}
.hero-title{position:absolute;top:400px;width:1200px;text-align:center;color:var(--white);font-family:var(--script);font-size:92px;line-height:1}
.hero-sub{position:absolute;top:545px;width:1200px;text-align:center;color:var(--white);font-size:15px;letter-spacing:4px;font-weight:600}
.hero-line{position:absolute;top:572px;left:440px;width:320px;height:1px;background:rgba(255,255,255,.5)}
.hero-tag{position:absolute;top:595px;width:1200px;text-align:center;color:var(--white);font-size:10px;letter-spacing:2px}

/* Intro */
.intro{top:680px;height:260px}
.intro p{position:absolute;left:90px;width:1010px;font-size:12px;line-height:20px;color:var(--muted)}

/* Services */
.services{top:940px;height:700px;background:var(--taupe)}
.card{position:absolute;top:100px;width:320px}
.card .photo{position:relative;height:220px;width:320px}
.card h3{margin-top:38px;font-size:26px;line-height:32px;font-weight:400;letter-spacing:2px;color:var(--white)}
.card p{margin-top:22px;font-size:11px;line-height:18px;color:#f3eeea}
.card .more{margin-top:28px;font-size:12px;letter-spacing:2px;color:var(--white)}
.pager{position:absolute;top:625px;left:1000px;font-size:10px;color:var(--white);letter-spacing:2px}

/* CTA */
.cta{top:1640px;height:230px;text-align:center}
.cta p{position:absolute;top:90px;width:1200px;font-size:11px;letter-spacing:2px;line-height:18px;color:var(--muted)}
.btn{display:inline-block;font-size:10px;letter-spacing:2px;color:var(--ink);border-bottom:1px solid var(--ink);padding-bottom:4px}
.cta .btn{position:absolute;top:145px;left:545px}

/* Reviews */
.reviews{top:1870px;height:670px}
.reviews .photo{inset:0;background:linear-gradient(180deg,#9b9089 0%,#bfb6ad 45%,#cfc8c0 70%,#b9b0a7 100%)}
.reviews .label{position:absolute;top:62px;left:90px;color:var(--white);font-size:12px;letter-spacing:3px;font-weight:600}
.reviews .all{position:absolute;top:58px;left:1010px;color:var(--white);font-size:10px;letter-spacing:2px;border-bottom:1px solid var(--white);padding-bottom:3px}
.couple-name{position:absolute;top:160px;left:90px;color:var(--white);font-family:var(--script);font-size:70px;line-height:80px}
.reviews .tag{position:absolute;top:330px;left:90px;color:var(--white);font-size:10px;letter-spacing:2px}
.reviews .play{left:556px;top:300px;width:76px;height:76px}
.reviews .quote{position:absolute;top:225px;left:780px;width:300px;color:var(--white);font-size:10px;line-height:16px;letter-spacing:1.5px}
.reviews .sign{position:absolute;top:330px;left:920px;color:var(--white);font-family:var(--script);font-size:40px}

/* Band */
.band{top:2540px;height:200px;background:var(--cream)}
.band .brand{top:62px;color:var(--gold)}
.band .brand .dot{background:var(--gold)}

/* Feature */
.feature{top:2740px;height:650px;background:var(--taupe)}
.feature .photo{left:90px;top:85px;width:600px;height:440px;background:linear-gradient(135deg,#d8c9b7 0%,#a08874 50%,#5e4c40 100%)}
.feature .panel{position:absolute;left:600px;top:130px;width:510px;height:460px;background:var(--white);padding:70px 50px}
.panel h2{font-size:22px;letter-spacing:3px;font-weight:400;color:var(--ink)}
.panel .lede{margin-top:24px;font-size:10px;line-height:16px;letter-spacing:1.5px;color:var(--gold)}
.panel .body{margin-top:26px;font-size:10px;line-height:16px;letter-spacing:1.5px;color:var(--muted)}
.panel .btn{margin-top:40px}

/* Footer */
footer{top:3390px;height:414px;background:var(--footer);color:#e9e2dc}
.company{position:absolute;top:40px;width:1200px;text-align:center;font-size:9px;letter-spacing:2px}
.col-title{position:absolute;top:140px;font-size:10px;letter-spacing:2px;font-weight:600}
.links{position:absolute;top:168px;left:90px;font-size:9px;line-height:15px;letter-spacing:1.5px}
.thumb{position:absolute;width:95px;height:58px}
.contact-line{position:absolute;left:600px;font-size:9px;letter-spacing:1.5px}
.contact-line svg{vertical-align:middle;margin-right:8px}
footer .brand{top:300px;left:570px;width:60px}
footer .brand span{font-size:11px}
footer .brand .dot{width:10px;height:10px}
.news p{position:absolute;top:168px;left:870px;width:230px;font-size:9px;line-height:15px;letter-spacing:1.5px}
.field{position:absolute;top:218px;left:870px;width:230px;border-bottom:1px solid #e9e2dc;font-size:9px;letter-spacing:1.5px;padding-bottom:5px}
.signup{position:absolute;top:245px;left:870px;width:64px;height:24px;border-radius:12px;background:var(--cream);color:var(--ink);font-size:9px;text-align:center;line-height:25px;letter-spacing:1px}
.legal{position:absolute;top:376px;font-size:8px;letter-spacing:1.5px}
.social{position:absolute;top:374px;width:12px;height:12px;border-radius:50%;border:1px solid #e9e2dc}
</style>
</head>
<body>

<header class="hero">
  <div class="photo" role="img" aria-label="Close-up of a groom placing a wedding ring on the bride's finger"></div>
  <nav class="nav">
    <a style="left:240px">FILMS</a>
    <a style="left:318px">PRICES</a>
    <a style="left:400px">REVIEWS</a>
    <div class="brand"><i class="dot"></i><span>BMTS</span></div>
    <a style="left:706px">OPTIONS</a>
    <a style="left:800px">ABOUT</a>
    <a style="left:880px">CONTACT</a>
  </nav>
  <div class="play"><svg width="84" height="84" viewBox="0 0 84 84"><path d="M35 28 L58 42 L35 56Z" fill="#fff"/></svg></div>
  <div class="hero-title">BMTS</div>
  <div class="hero-sub">OPTIONS</div>
  <div class="hero-line"></div>
  <div class="hero-tag">WEDDING VIDEOGRAPHY · NORTH EAST, UK AND WORLDWIDE FILMS</div>
</header>

<section class="intro">
  <p style="top:90px">Your wedding day is a once in a lifetime moment. A moment in time where all the people you love and care about are in the same place at the same time. We document unique moments on film. The laughs, the tears and the love.</p>
  <p style="top:150px">The films we make will last a lifetime. They will be shown to future generations and will become an heirloom. It will be watched over and over again over the years. Your memories of your day will hold forever, our wedding films will ensure you never forget those moments.</p>
</section>

<section class="services">
  <article class="card" style="left:90px">
    <div class="photo" role="img" aria-label="Bride's hands holding a ring" style="background:linear-gradient(135deg,#f2ece7,#c9b5a5)"></div>
    <h3>CINEMATIC<br>HIGHLIGHTS FILM</h3>
    <p>A highlights film is the heart of our story, moving music and cinematic edits bring it all together in a few minutes. Every look, laugh and tear from your day is kept in a piece you will watch for years and share with family across generations.</p>
  </article>
  <article class="card" style="left:440px">
    <div class="photo" role="img" aria-label="Couple at the altar during a church ceremony" style="background:linear-gradient(180deg,#6b5446,#a99282)"></div>
    <h3>CEREMONY AND<br>SPEECHES</h3>
    <p>Watch the full ceremony and your speeches in full, just as they were heard in the room. Every vow, every toast and every joke is recorded with clear sound and edited with care, so nothing said on the day is ever lost to memory.</p>
  </article>
  <article class="card" style="left:790px">
    <div class="photo" role="img" aria-label="Couple walking on a sunny beach" style="background:linear-gradient(180deg,#8fb7d6,#e8dccb)"></div>
    <h3>OUR STORY FEATURE</h3>
    <p>A feature length film that tells your story from start to end. Getting ready, the ceremony, the speeches and the first dance are all woven into one film you can settle down and enjoy again and again.</p>
    <div class="more">OPTIONAL</div>
  </article>
  <div class="pager">PREV — NEXT</div>
</section>

<section class="cta">
  <p>I'D LOVE TO HEAR FROM YOU IF YOU ARE GETTING MARRIED.<br>PLEASE FOLLOW THE LINK BELOW TO CHECK MY AVAILABILITY.</p>
  <span class="btn">CONTACT US</span>
</section>

<section class="reviews">
  <div class="photo" role="img" aria-label="Bride in a white dress holding a bouquet on a beach"></div>
  <div class="label">REVIEWS</div>
  <div class="all">VIEW ALL</div>
  <div class="couple-name">Lena<br>Marsh</div>
  <div class="tag">COAST WEDDING</div>
  <div class="play"><svg width="72" height="72" viewBox="0 0 72 72"><path d="M30 24 L50 36 L30 48Z" fill="#fff"/></svg></div>
  <p class="quote">WE ARE SO HAPPY WITH OUR FILM. IT CAPTURED EVERY MOMENT OF THE DAY PERFECTLY AND WE CRY EVERY TIME WE WATCH IT. THANK YOU FOR BEING PART OF OUR DAY AND FOR MAKING US FEEL SO AT EASE.</p>
  <div class="sign">Lena</div>
</section>

<section class="band">
  <div class="brand"><i class="dot"></i><span>BMTS</span></div>
</section>

<section class="feature">
  <div class="photo" role="img" aria-label="Bride and groom embracing outdoors"></div>
  <div class="panel">
    <h2>BMTS FILM</h2>
    <p class="lede">I'D LOVE TO HEAR FROM YOU IF YOU ARE GETTING MARRIED. PLEASE FOLLOW THE LINK BELOW TO CHECK MY DATES.</p>
    <p class="body">EVERY FILM IS MADE WITH CARE, FROM THE FIRST CALL TO THE FINAL EDIT. WE TRAVEL ACROSS THE UK AND EUROPE TO TELL YOUR STORY IN A STYLE THAT FEELS NATURAL, CALM AND TRUE TO YOU BOTH.</p>
    <span class="btn">CONTACT US</span>
  </div>
</section>

<footer>
  <div class="company">BMTS FILMS LIMITED</div>

  <div class="col-title" style="left:90px">LINKS</div>
  <div class="links">BLOG<br>PRICES<br>LOVE STORIES<br>REVIEWS<br>BEHIND THE SCENES<br>CONTACT</div>

  <div class="thumb" role="img" aria-label="Wedding film still" style="left:225px;top:165px;background:#6d5a4e"></div>
  <div class="thumb" role="img" aria-label="Wedding film still" style="left:330px;top:165px;background:#8a7868"></div>
  <div class="thumb" role="img" aria-label="Wedding film still" style="left:225px;top:233px;background:#9c8877"></div>
  <div class="thumb" role="img" aria-label="Wedding film still" style="left:330px;top:233px;background:#5f4f45"></div>

  <div class="col-title" style="left:600px">CONTACT</div>
  <div class="contact-line" style="top:172px"><svg width="10" height="10" viewBox="0 0 10 10"><path d="M2 1 L4 1 L5 3 L4 4 Q5 6 6 6 L7 5 L9 6 L9 8 Q5 9 2 5 Q1 3 2 1Z" fill="#e9e2dc"/></svg>01632 960 214</div>
  <div class="contact-line" style="top:192px"><svg width="10" height="10" viewBox="0 0 10 10"><rect x="0.5" y="2" width="9" height="6" fill="none" stroke="#e9e2dc"/><path d="M0.5 2 L5 5.5 L9.5 2" fill="none" stroke="#e9e2dc"/></svg>HELLO@BMTSFILMS.CO.UK</div>
  <div class="brand"><i class="dot"></i><span>BMTS</span></div>

  <div class="col-title" style="left:870px">NEWSLETTER</div>
  <div class="news"><p>WOULD YOU LIKE US TO SEND YOU NEWS, SPECIAL OFFERS &amp; TIPS BY EMAIL?</p></div>
  <div class="field">EMAIL ADDRESS</div>
  <div class="signup">SIGN UP</div>

  <div class="legal" style="left:90px">COPYRIGHT © 2024 BMTS</div>
  <div class="legal" style="left:430px">WEDDING VIDEOGRAPHY · NORTH EAST, UK AND WORLDWIDE FILMS</div>
  <span class="social" style="left:1052px"></span>
  <span class="social" style="left:1072px"></span>
  <span class="social" style="left:1092px"></span>
</footer>

</body>
</html>
```